Marlowe Holdings LLC - Business Cards

Need the following information on the cards:

Name: Dean R Vossler
Title: Chief Executive Manager

Business address:
412 N Ridgeview Lane #118
Brookhaven Falls, Il 60412

Phone: (555) 555-0148 - Business
KPV FFL license number: 5-21-xxx-xx-xx-04519
Email: dean.vossler@marloweholdingsffl.com

Target Market(s)

Firearm owners

Industry/Entity Type

Firearms industry,

Contact Information for Business Card

Contact number, name and title, web page address, email, business address and kpv license number,

Requirements
Must have
• Name, title, business address, phone numbers, KPV license numbers, web page address and email address.
Nice to have
• Cellphone number,

```html
<!DOCTYPE html>
<html lang="en">
<head>
<meta charset="utf-8">
<title>Marlowe Holdings LLC – Business Cards</title>
<link rel="stylesheet" href="https://fonts.googleapis.com/css2?family=Josefin+Sans:wght@400;600;700&display=swap">
<style>
  :root {
    --page: #ffffff;
    --card-dark: #000000;
    --card-red: #cc1e24;
    --brand-red: #d42027;
    --ink-light: #ffffff;
    --ink-dark: #111111;
  }
  * { margin: 0; padding: 0; box-sizing: border-box; }
  html, body {
    width: 1200px; height: 459px; overflow: hidden;
    background: var(--page);
    font-family: "Josefin Sans", sans-serif;
  }
  .canvas { position: relative; width: 1200px; height: 459px; }

  .card {
    position: absolute; top: 78px; height: 302px;
    box-shadow: 0 22px 18px -14px rgba(0,0,0,0.28);
  }
  .card-front { left: 90px; width: 510px; background: var(--card-dark); color: var(--ink-light); }
  .card-back { left: 643px; width: 467px; background: var(--card-red); }

  .holder { position: absolute; left: 17px; top: 132px; }
  .holder-name {
    font-size: 25px; font-weight: 600; letter-spacing: 1.5px; text-transform: uppercase; line-height: 1;
  }
  .holder-title {
    margin-top: 6px; padding-left: 25px;
    font-size: 8px; font-weight: 600; letter-spacing: 2.4px; text-transform: uppercase;
  }

  .brand-mark {
    position: absolute; display: flex; flex-direction: column; align-items: center;
    font-weight: 700; text-transform: uppercase; line-height: 1;
  }
  .brand-mark-front { left: 270px; top: 70px; width: 190px; color: var(--brand-red); }
  .brand-mark-front .brand-word { font-size: 30px; letter-spacing: 1px; }
  .brand-mark-front .brand-sub { font-size: 12px; letter-spacing: 2.5px; margin-top: 6px; }
  .brand-mark-back { left: 0; right: 0; top: 112px; color: var(--ink-light); }
  .brand-mark-back .brand-word { font-size: 44px; letter-spacing: 2px; }
  .brand-mark-back .brand-sub { font-size: 16px; letter-spacing: 4px; margin-top: 10px; }
  .brand-dot {
    width: 14px; height: 14px; border-radius: 50%; background: currentColor; margin-bottom: 10px;
  }

  .contacts {
    position: absolute; right: 68px; top: 202px;
    list-style: none; text-align: right;
    font-size: 10px; font-weight: 600; letter-spacing: 0.5px; line-height: 1.25;
    font-variant: small-caps;
  }
  .contact { display: flex; justify-content: flex-end; align-items: center; gap: 7px; margin-bottom: 5px; }
  .contact-email { text-transform: lowercase; margin-bottom: 10px; }
  .contact-icon { width: 15px; height: 15px; flex: none; }
</style>
</head>
<body>
<main class="canvas">
  <section class="card card-front" aria-label="Business card front">
    <div class="brand-mark brand-mark-front">
      <span class="brand-dot"></span>
      <span class="brand-word">Marlowe</span>
      <span class="brand-sub">Holdings LLC</span>
    </div>

    <div class="holder">
      <p class="holder-name">Dean R Vossler</p>
      <p class="holder-title">Chief Executive Manager</p>
    </div>

    <ul class="contacts">
      <li class="contact contact-email">
        <span>dean.vossler@marloweholdingsffl.com</span>
        <svg class="contact-icon" viewBox="0 0 16 16" aria-hidden="true"><circle cx="8" cy="8" r="8" fill="#fff"/><circle cx="8" cy="8" r="2.2" fill="none" stroke="#111" stroke-width="1.3"/><path d="M10.2 6v3c0 1.3 2 1.3 2 -1 A4.2 4.2 0 1 0 9.8 11.8" fill="none" stroke="#111" stroke-width="1.3"/></svg>
      </li>
      <li class="contact">
        <span>5-21-xxx-xx-xx-04519</span>
        <svg class="contact-icon" viewBox="0 0 16 16" aria-hidden="true"><circle cx="8" cy="8" r="8" fill="#fff"/><rect x="3.5" y="5" width="9" height="6.5" rx="1" fill="none" stroke="#111" stroke-width="1.1"/><circle cx="6" cy="7.5" r="1" fill="#111"/><path d="M8.5 7h3M8.5 9h3" stroke="#111" stroke-width="1"/></svg>
      </li>
      <li class="contact">
        <span>412 N Ridgeview Lane #118<br>Brookhaven Falls, Il 60412</span>
        <svg class="contact-icon" viewBox="0 0 16 16" aria-hidden="true"><circle cx="8" cy="8" r="8" fill="#fff"/><path d="M8 13s-3.5-3.6-3.5-6a3.5 3.5 0 0 1 7 0c0 2.4-3.5 6-3.5 6z" fill="#111"/><circle cx="8" cy="7" r="1.3" fill="#fff"/></svg>
      </li>
      <li class="contact">
        <span>(555) 555-0148</span>
        <svg class="contact-icon" viewBox="0 0 16 16" aria-hidden="true"><circle cx="8" cy="8" r="8" fill="#fff"/><path d="M5.2 3.8l1.6 2.1-.9 1.1c.6 1.2 1.5 2.1 2.7 2.7l1.1-.9 2.1 1.6-.9 1.6c-3.3.1-6.4-3-6.3-6.3z" fill="#111"/></svg>
      </li>
    </ul>
  </section>

  <section class="card card-back" aria-label="Business card back">
    <div class="brand-mark brand-mark-back">
      <span class="brand-dot"></span>
      <span class="brand-word">Marlowe</span>
      <span class="brand-sub">Holdings LLC</span>
    </div>
  </section>
</main>
</body>
</html>
```